Easy one-page Web Design with ready made sketch/template

This project have an already made one page Web Design sketch/template that should be used as a base. It needs professional touch and improvements but should be quite straight forward for you to make.

Webpage: Offers local graphical design services

Attached following documents for you:
- PSD sketch
- JPG sketch
- Word file with project description (read carefully)
- Logo

Reason: Project extended to get the final designs submitted. Thanks

Target Market(s)

Logo design

Industry/Entity Type

Graphic Design

Number of Pages Required

1 page

Requirements
Must have
• Please refer to attached word document.
Nice to have
Should not have

```html
<!DOCTYPE html>
<html lang="sv">
<head>
<meta charset="utf-8">
<title>Formverk – Ny Logotyp</title>
<link rel="stylesheet" href="https://fonts.googleapis.com/css2?family=Montserrat:wght@400;600;700;800&family=Open+Sans:wght@400;600;700&family=Rubik:ital,wght@1,800&display=swap">
<style>
:root{
  --side:#b7b7b7;
  --dark:#1f2328;
  --darker:#121417;
  --blue:#1e8fdc;
  --blue-deep:#1565b8;
  --blue-light:#d8ecf8;
  --sky:#3a9be0;
  --yellow:#f5c518;
  --grey:#e4e4e4;
  --grey-mid:#c9c9c9;
  --text:#333;
  --muted:#8a8a8a;
  --white:#fff;
}
*{box-sizing:border-box;margin:0;padding:0}
html,body{width:1200px;height:5143px;overflow:hidden}
body{background:linear-gradient(90deg,#a9a9a9,#c4c4c4 15%,#c4c4c4 85%,#a9a9a9);font-family:"Open Sans",Arial,sans-serif;color:var(--text);position:relative}
.page{position:absolute;left:178px;top:0;width:844px;background:var(--white)}
section,header,footer{position:relative;overflow:hidden}
.ph{display:block}
.btn{display:inline-block;background:var(--blue);color:var(--white);font:700 11px "Montserrat",sans-serif;letter-spacing:.5px;padding:8px 22px;border-radius:14px}
.h-script{font:italic 800 30px "Rubik",sans-serif;color:var(--blue-deep);text-align:center;letter-spacing:1px}
.h-caps{font:800 20px "Montserrat",sans-serif;color:var(--blue);text-align:center;letter-spacing:1px}

/* nav */
.topbar{height:45px;background:var(--dark);display:flex;align-items:center;padding:0 40px;gap:30px}
.brand{display:flex;align-items:center;gap:8px;font:700 16px "Montserrat",sans-serif;color:var(--white)}
.brand i{width:14px;height:14px;background:var(--blue);display:block}
.nav{display:flex;gap:28px;margin-left:90px;font:600 11px "Montserrat",sans-serif;color:var(--white)}
.topbar .btn{margin-left:auto;padding:5px 14px;font-size:9px}
.callus{font:600 10px "Montserrat",sans-serif;color:var(--white)}

/* hero */
.hero{height:418px;text-align:center;color:var(--white)}
.hero .ph{position:absolute;inset:0;background:linear-gradient(160deg,#6e7c88,#c9cfd4 45%,#8d9aa5 70%,#3e4a55)}
.hero-body{position:relative;padding-top:100px}
.hero h1{font:700 34px "Montserrat",sans-serif;text-shadow:0 2px 6px rgba(0,0,0,.35)}
.hero p{font-size:13px;margin:12px auto 0;width:460px;line-height:1.4}
.hero .outline{display:inline-block;margin-top:22px;border:2px solid var(--white);border-radius:16px;padding:7px 22px;font:700 10px "Montserrat",sans-serif}
.hero .from{margin-top:28px;font:700 13px "Montserrat",sans-serif;letter-spacing:1px}

.notes{height:240px}
.notes .ph{position:absolute;inset:0;background:linear-gradient(180deg,#4a3c30,#6b5544 50%,#3b2f26)}

/* packages */
.packages{height:539px;background:linear-gradient(160deg,#5fb3ea,#2f8fd6 45%,#7cc3ef)}
.ribbon{position:absolute;left:50%;top:10px;transform:translateX(-50%);background:var(--blue-deep);padding:8px 30px;border-radius:4px}
.ribbon .h-script{color:var(--white);font-size:24px}
.card{position:absolute;top:88px;width:155px;height:380px;background:var(--white);border-radius:4px;box-shadow:0 4px 10px rgba(0,0,0,.2);text-align:center;padding-top:0}
.card h3{background:var(--blue);color:var(--white);font:700 13px "Montserrat",sans-serif;padding:10px 0 10px 14px;text-align:left}
.card .price{font:600 15px "Montserrat",sans-serif;color:#555;margin:22px 0 16px}
.card li{list-style:none;font-size:8px;color:#555;line-height:26px;border-bottom:1px solid #eee;margin:0 16px;text-align:left}
.card .btn{position:absolute;bottom:20px;left:50%;transform:translateX(-50%);font-size:9px;padding:6px 18px}
.card.featured{top:58px;width:175px;height:440px}
.card.featured h3{background:var(--yellow);color:var(--dark);text-align:center;padding:12px 0}
.card.featured .btn{background:var(--yellow);color:var(--dark)}

/* reviews */
.reviews{height:398px;background:repeating-linear-gradient(45deg,#e6eef5 0 10px,#f3f7fb 10px 20px)}
.reviews .h-script{position:absolute;left:96px;top:10px;font-size:24px;color:var(--dark)}
.review{position:absolute;left:96px;width:430px;height:82px;background:var(--white);border:3px solid #bcd6ee;border-radius:8px;padding:12px 16px 0 80px}
.review .avatar{position:absolute;left:20px;top:14px;width:46px;height:46px;border-radius:50%;background:linear-gradient(#8a6a55,#4c3a30)}
.review b{font:700 10px "Montserrat",sans-serif}
.stars{color:var(--yellow);font-size:10px;letter-spacing:1px}
.review p{font-size:8px;color:var(--muted);line-height:1.4}
.reviews .photo{position:absolute;right:0;top:0;width:240px;height:398px;background:linear-gradient(170deg,#5b6c7c,#9aa8b4 55%,#2e3a46)}
.medal{position:absolute;left:520px;top:26px;width:70px;height:70px;border-radius:50%;background:#2c2c2c;border:4px solid #9c9c9c}

/* why */
.why{height:425px;background:var(--white)}
.why::after{content:"";position:absolute;right:0;top:60px;border-style:solid;border-width:0 110px 300px 0;border-color:transparent #f9d97a transparent transparent}
.why .h-script{padding-top:30px;font-size:28px}
.why .sub{text-align:center;font:700 11px "Montserrat",sans-serif;color:var(--dark);margin-top:6px}
.why .photo{position:absolute;left:79px;top:120px;width:240px;height:280px;background:linear-gradient(150deg,#7a6a5c,#d9d2c6 50%,#8a7a6a)}
.tiles{position:absolute;left:336px;top:120px;width:412px;display:grid;grid-template-columns:1fr 1fr;gap:8px;z-index:1}
.tile{height:88px;background:var(--sky);display:flex;gap:10px;padding:12px;color:var(--white)}
.tile.alt{background:#1f6fb7}
.tile svg{flex:none}
.tile b{display:block;font:700 9px "Montserrat",sans-serif}
.tile span{font-size:8px;line-height:1.4}

/* latest logos */
.latest{height:391px;background:#cfe6f6;text-align:center}
.latest .h-caps{padding-top:38px;color:var(--white);background:none}
.latest .label{display:inline-block;margin-top:40px;background:var(--blue);color:var(--white);font:800 18px "Montserrat",sans-serif;padding:6px 26px;letter-spacing:1px}
.carousel{position:absolute;top:150px;left:70px;right:70px;height:170px;display:flex;align-items:center;justify-content:center;gap:6px}
.logo-tile{width:120px;height:130px;display:flex;align-items:center;justify-content:center;font:700 18px "Montserrat",sans-serif}
.logo-tile.big{width:190px;height:170px;background:#000;color:var(--white);font-size:24px}
.arrow{position:absolute;top:220px;width:28px;height:28px;border-radius:50%;background:#9bb7cc;color:var(--white);font:700 16px/28px sans-serif}
.latest .btn{position:absolute;left:50%;bottom:20px;transform:translateX(-50%);background:var(--yellow);color:var(--dark)}

/* order */
.order{height:844px;background:var(--grey)}
.order .h-caps{padding-top:38px;font-size:22px}
.order .sub{text-align:center;font:700 11px "Montserrat",sans-serif;color:var(--dark);margin-top:4px}
.testis{position:absolute;left:34px;top:130px;width:165px}
.testi{background:var(--white);border-radius:4px;padding:12px;margin-bottom:14px;height:200px}
.testi:first-child{height:120px;text-align:center}
.testi .av{width:34px;height:34px;border-radius:50%;background:linear-gradient(#8a6a55,#4c3a30);float:left;margin-right:8px}
.testi b{font:700 8px "Montserrat",sans-serif}
.testi p{clear:both;font-size:7px;color:var(--muted);line-height:1.5;padding-top:8px}
.testi .bars{clear:both;margin-top:10px;height:120px;background:repeating-linear-gradient(180deg,#e2e2e2 0 5px,transparent 5px 10px)}
.form{position:absolute;left:216px;top:130px;width:573px;height:660px;background:#8f8f8f;border-radius:6px;padding:30px 40px;color:var(--white)}
.form label{display:block;font:700 9px "Montserrat",sans-serif;margin-bottom:8px}
.field{height:28px;background:var(--white);border-radius:14px;color:#aaa;font-size:10px;padding:7px 14px;margin-bottom:42px}
.row{display:flex;gap:40px}.row>div{flex:1}
.area{height:150px;background:var(--white);border-radius:6px}
.radios{columns:2;font-size:8px;line-height:33px}
.radios i{display:inline-block;width:14px;height:14px;border-radius:50%;background:var(--white);vertical-align:middle;margin-right:8px}
.form .note{font-size:7px;opacity:.8;margin-top:10px}
.form .btn{position:absolute;left:50%;bottom:30px;transform:translateX(-50%)}

/* products */
.products{height:473px;text-align:center;background:var(--white)}
.products .h-script{padding-top:30px;color:var(--dark)}
.products .sub{font:700 11px "Montserrat",sans-serif;color:var(--dark);margin-top:4px}
.grid5{display:grid;grid-template-columns:repeat(5,120px);justify-content:center;margin-top:40px}
.prod{height:110px;border-right:1px solid #ddd;border-bottom:1px solid #ddd;padding-top:24px;font:600 7px "Montserrat",sans-serif;color:#555}
.prod:nth-child(5n){border-right:0}.prod:nth-child(n+6){border-bottom:0}
.prod svg{display:block;margin:0 auto 10px}
.products .btn{margin-top:30px}

/* projects */
.projects{height:257px;background:var(--white);text-align:center}
.projects .h-caps{font-size:14px;padding-top:10px}
.projects .sub{font-size:8px;color:var(--muted)}
.prow{display:flex;justify-content:center;align-items:center;gap:20px;margin-top:40px;font:700 13px "Montserrat",sans-serif;color:var(--blue-deep)}
.prow .alt{color:#d23a2a}
.dots{margin-top:30px;display:flex;justify-content:center;gap:6px}
.dots i{width:7px;height:7px;border-radius:50%;background:#bcd6ee}.dots i:first-child{background:var(--blue)}
.projects .btn{margin-top:20px}
.projects .arrow{background:none;color:#999;top:80px}

/* questions */
.questions{height:412px;background:var(--white)}
.questions .person{position:absolute;left:40px;top:40px;width:180px;height:330px;background:linear-gradient(#c08a5a,#e0b46a 60%,#8f7a60);border-radius:40px 40px 10px 10px}
.q-text{position:absolute;left:250px;top:40px;width:200px}
.q-text h2{font:600 22px "Montserrat",sans-serif;color:#7a4a3a}
.q-text p{font-size:9px;color:#666;line-height:1.5;margin-top:12px}
.q-text .ln{font-size:9px;color:#b04030;margin-top:8px}
.q-form{position:absolute;left:470px;top:40px;width:320px;height:330px;background:var(--grey);border-radius:6px}
.q-form h4{background:var(--sky);color:var(--white);font:700 10px "Montserrat",sans-serif;padding:14px;border-radius:6px 6px 0 0}
.q-form .f{height:22px;background:var(--white);border-radius:11px;margin:14px 24px 0}

/* feed */
.feed{height:360px;background:linear-gradient(#e3f1fa,#c3e0f3);text-align:center}
.feed h3{padding-top:28px;font:400 22px "Montserrat",sans-serif;color:var(--dark);display:flex;justify-content:center;align-items:center;gap:10px}
.feed h3 i{width:22px;height:22px;border:2px solid var(--dark);display:block}
.feed .prow{margin-top:30px;flex-wrap:wrap;width:620px;margin-left:auto;margin-right:auto;row-gap:30px}
.feed .btn{margin-top:34px;background:var(--dark)}

/* social + footer */
.social{height:62px;background:var(--dark);display:flex;justify-content:center;align-items:center;gap:28px;font:600 9px "Montserrat",sans-serif;color:var(--white)}
.social span::before{content:"";display:inline-block;width:16px;height:16px;border-radius:50%;background:#3a3f46;vertical-align:middle;margin-right:6px}
.fnav{height:41px;background:#2a2e33;display:flex;justify-content:center;align-items:center;gap:40px;font:600 9px "Montserrat",sans-serif;color:var(--blue)}
.footer{height:205px;background:var(--darker);color:#bbb;display:flex;gap:40px;padding:30px 50px;font-size:8px;line-height:1.7}
.footer h5{font:700 9px "Montserrat",sans-serif;color:var(--white);margin-bottom:10px}
.footer .in{width:150px;height:18px;background:var(--white);border-radius:2px;margin-top:8px}
.footer .brand{font-size:14px;margin-bottom:6px}
</style>
</head>
<body>
<div class="page">

<header class="topbar">
  <div class="brand"><i></i>Formverk</div>
  <nav class="nav"><span>Products</span><span>Gallery</span><span>FAQ</span><span>Contact us</span></nav>
  <span class="btn">ORDER NOW</span>
  <span class="callus">Call us: 08-555 01 23</span>
</header>

<section class="hero">
  <div class="ph" role="img" aria-label="Photo of a designer's desk with sketchbook and coffee cup"></div>
  <div class="hero-body">
    <h1>Ny Logotyp – Företagslogga?</h1>
    <p>We design your professional company logo fast and send you the first drafts already within 24 hours</p>
    <span class="outline">ORDER NOW</span>
    <div class="from">START FROM 1495 $</div>
  </div>
</section>

<section class="notes">
  <div class="ph" role="img" aria-label="Photo of sticky notes on a wooden table listing service benefits"></div>
</section>

<section class="packages">
  <div class="ribbon"><div class="h-script">Select a Package</div></div>
  <div class="card" style="left:38px"><h3>STARTER</h3><div class="price">1495 $ +MOMS</div>
    <ul><li>2 LOGOTYPFÖRSLAG</li><li>1 ÄNDRINGSRUNDA</li><li>FILER FÖR WEBBEN</li></ul><span class="btn">BESTÄLL</span></div>
  <div class="card" style="left:233px"><h3>SILVER</h3><div class="price">2495 $ +MOMS</div>
    <ul><li>4 LOGOTYPFÖRSLAG</li><li>3 ÄNDRINGSRUNDOR</li><li>FILER FÖR WEBBEN</li><li>FILER FÖR TRYCK</li><li>VISITKORT</li><li>BREVPAPPER</li></ul><span class="btn">BESTÄLL</span></div>
  <div class="card featured" style="left:422px"><h3>UNLIMITED</h3><div class="price">3995:- (ORD.<br>7995 6995:-)</div>
    <ul><li>FRIA LOGOTYPFÖRSLAG</li><li>FRIA ÄNDRINGSRUNDOR</li><li>FILER FÖR WEBBEN</li><li>FILER FÖR TRYCK</li><li>VISITKORT</li><li>BREVPAPPER</li><li>GRAFISK PROFIL</li></ul><span class="btn">BESTÄLL</span></div>
  <div class="card" style="left:628px"><h3>PLATINUM</h3><div class="price">9995 $ +MOMS</div>
    <ul><li>FRIA LOGOTYPFÖRSLAG</li><li>FRIA ÄNDRINGSRUNDOR</li><li>FILER FÖR WEBBEN</li><li>FILER FÖR TRYCK</li><li>HEMSIDA</li><li>GRAFISK PROFIL</li></ul><span class="btn">BESTÄLL</span></div>
</section>

<section class="reviews">
  <div class="h-script">Customer Reviews</div>
  <div class="medal"></div>
  <div class="review" style="top:70px"><span class="avatar" role="img" aria-label="Customer portrait"></span><b>Super nöjd kund</b> <span class="stars">★★★★★</span><p>Snabb leverans och fina förslag. Vi fick precis den logga vi ville ha för vårt företag.</p></div>
  <div class="review" style="top:166px"><span class="avatar" role="img" aria-label="Customer portrait"></span><b>Super nöjd kund</b> <span class="stars">★★★★★</span><p>Proffsigt bemötande hela vägen och ett resultat som överträffade våra förväntningar.</p></div>
  <div class="review" style="top:262px"><span class="avatar" role="img" aria-label="Customer portrait"></span><b>Super nöjd kund</b> <span class="stars">★★★★★</span><p>Enkelt att beställa och ändringarna gjordes samma dag. Rekommenderas varmt.</p></div>
  <div class="photo" role="img" aria-label="Photo of a smiling businessman giving a thumbs up"></div>
</section>

<section class="why">
  <div class="h-script">Why Choose Us ?</div>
  <div class="sub">100% SATISFACTION</div>
  <div class="photo" role="img" aria-label="Photo of hands sketching on paper at a desk"></div>
  <div class="tiles">
    <div class="tile"><svg width="26" height="26" viewBox="0 0 26 26"><path d="M5 13l6 6 10-12" fill="none" stroke="#fff" stroke-width="3"/></svg><div><b>PROFESSIONAL DESIGNERS</b><span>Erfarna formgivare som skapar unika loggor.</span></div></div>
    <div class="tile alt"><svg width="26" height="26" viewBox="0 0 26 26"><circle cx="13" cy="13" r="10" fill="none" stroke="#fff" stroke-width="2.5"/><path d="M13 7v6l4 3" stroke="#fff" stroke-width="2.5" fill="none"/></svg><div><b>FAST DELIVERY</b><span>Första förslagen inom 24 timmar.</span></div></div>
    <div class="tile alt"><svg width="26" height="26" viewBox="0 0 26 26"><path d="M4 20h18M7 20V10M13 20V5M19 20v-7" stroke="#fff" stroke-width="3"/></svg><div><b>FAIR PRICES</b><span>Fasta priser utan dolda avgifter.</span></div></div>
    <div class="tile"><svg width="26" height="26" viewBox="0 0 26 26"><path d="M13 2l3 8h8l-6 5 2 9-7-5-7 5 2-9-6-5h8z" fill="#f5c518"/></svg><div><b>TOP RATED</b><span>Hundratals nöjda kunder varje år.</span></div></div>
    <div class="tile"><svg width="26" height="26" viewBox="0 0 26 26"><rect x="4" y="6" width="18" height="14" rx="2" fill="none" stroke="#fff" stroke-width="2.5"/></svg><div><b>ALL FILE FORMATS</b><span>Färdiga filer för webb och tryck.</span></div></div>
    <div class="tile alt"><svg width="26" height="26" viewBox="0 0 26 26"><circle cx="13" cy="13" r="10" fill="#f28fb0"/></svg><div><b>MONEY BACK</b><span>Nöjd kund eller pengarna tillbaka.</span></div></div>
  </div>
</section>

<section class="latest">
  <span class="label">LATEST LOGOS</span>
  <div class="carousel">
    <div class="logo-tile" style="background:#1b1b1b;color:#fff;width:100px;height:110px;font-size:13px">Stratos</div>
    <div class="logo-tile" style="background:#bfe6ee;color:#fff">Varde</div>
    <div class="logo-tile big">Norrvik AB</div>
    <div class="logo-tile" style="background:#222;color:#fff">Lunaro</div>
    <div class="logo-tile" style="background:#f4f4f4;color:#1e4fa0;width:100px;height:110px;font-size:13px">Bergsö</div>
  </div>
  <span class="arrow" style="left:10px">‹</span><span class="arrow" style="right:10px">›</span>
  <span class="btn">OUR GALLERY</span>
</section>

<section class="order">
  <div class="h-caps">ORDER LOGO</div>
  <div class="sub">FILL IN THE FORM AND GET STARTED</div>
  <div class="testis">
    <div class="testi"><b>LOREM IPSUM<br>DOLOR SIT AMET<br>CONSECTETUR ADIPISCING ELIT</b><div class="stars">★★★★★</div></div>
    <div class="testi"><span class="av" role="img" aria-label="Customer portrait"></span><b>Anna Berg</b><div class="stars">★★★★★</div><div class="bars"></div></div>
    <div class="testi"><span class="av" role="img" aria-label="Customer portrait"></span><b>Johan Lind</b><div class="stars">★★★★★</div><div class="bars"></div></div>
  </div>
  <div class="form">
    <label>LOREM IPSUM DOLOR</label><div class="field">Lorem ipsum dolor</div>
    <div class="row"><div><label>CONSECTETUR ADIPISCING</label><div class="field"></div></div><div><label>CONSECTETUR ADIPISCING</label><div class="field"></div></div></div>
    <div class="row"><div><label>QUIS NOSTRUD EXERCITATION</label><div class="area"></div><div class="note">Ut enim ad minim veniam quis</div></div>
      <div><label>QUIS NOSTRUD EXERCITATION</label><div class="radios"><div><i></i>Lorem</div><div><i></i>Ipsum</div><div><i></i>Dolor</div><div><i></i>Amet</div><div><i></i>Lorem</div><div><i></i>Ipsum</div><div><i></i>Dolor</div><div><i></i>Amet</div></div><div class="note">Ut enim ad minim veniam quis</div></div></div>
    <span class="btn">BESTÄLL</span>
  </div>
</section>

<section class="products">
  <div class="h-script">Products</div>
  <div class="sub">WE DO MORE THAN LOGOS</div>
  <div class="grid5">
    <div class="prod"><svg width="26" height="26"><rect x="4" y="4" width="18" height="18" fill="none" stroke="#777" stroke-width="2"/></svg>LOGO DESIGN</div>
    <div class="prod"><svg width="26" height="26"><rect x="2" y="5" width="22" height="14" fill="none" stroke="#777" stroke-width="2"/><path d="M8 23h10" stroke="#777" stroke-width="2"/></svg>WEB DESIGN</div>
    <div class="prod"><svg width="26" height="26"><rect x="3" y="7" width="20" height="12" fill="none" stroke="#777" stroke-width="2"/></svg>BUSINESS CARD &amp; LETTERHEAD</div>
    <div class="prod"><svg width="26" height="26"><path d="M5 21L19 7l2 2L7 23z" fill="none" stroke="#777" stroke-width="2"/></svg>ART &amp; ILLUSTRATION</div>
    <div class="prod"><svg width="26" height="26"><path d="M3 9l10-5 10 5v11l-10 4-10-4z" fill="none" stroke="#777" stroke-width="2"/></svg>PACKING &amp; LABEL</div>
    <div class="prod"><svg width="26" height="26"><path d="M3 5h9v17H3zM14 5h9v17h-9z" fill="none" stroke="#777" stroke-width="2"/></svg>BOOK &amp; MAGAZINE</div>
    <div class="prod"><svg width="26" height="26"><rect x="5" y="3" width="16" height="20" fill="none" stroke="#777" stroke-width="2"/></svg>BUSINESS &amp; ADVERTISING</div>
    <div class="prod"><svg width="26" height="26"><path d="M8 3l-6 5 3 4 3-2v13h10V10l3 2 3-4-6-5h-10z" fill="none" stroke="#777" stroke-width="2"/></svg>CLOTHING &amp; MERCHANDISE</div>
    <div class="prod"><svg width="26" height="26"><rect x="6" y="3" width="14" height="20" fill="none" stroke="#777" stroke-width="2"/></svg>BOOK COVER</div>
    <div class="prod"><svg width="26" height="26"><circle cx="13" cy="13" r="9" fill="none" stroke="#777" stroke-width="2"/></svg>OTHER</div>
  </div>
  <span class="btn">SHOW MORE</span>
</section>

<section class="projects">
  <div class="h-caps">LATEST PROJECTS</div>
  <div class="sub">Välj ett exempel</div>
  <span class="arrow" style="left:20px">‹</span><span class="arrow" style="right:20px">›</span>
  <div class="prow"><span>Solvik</span><span class="alt">Fjällström</span><span>Glimt</span><span>Brovik</span><span class="alt">Norda26</span></div>
  <div class="dots"><i></i><i></i><i></i><i></i><i></i></div>
  <span class="btn">SHOW MORE</span>
</section>

<section class="questions">
  <div class="person" role="img" aria-label="Photo of a smiling woman sitting with a laptop"></div>
  <div class="q-text">
    <h2>Questions?</h2>
    <p>Our support guys are here to help you with any design enlightenment. Check out our FAQs, send us an email, or give us a call.</p>
    <div class="ln">☎ 08-555 01 23</div>
    <div class="ln">✎ Free design consultation</div>
  </div>
  <div class="q-form">
    <h4>Lorem ipsum dolor sit amet, consectetur ?</h4>
    <div class="f"></div><div class="f"></div><div class="f"></div><div class="f"></div><div class="f"></div>
  </div>
</section>

<section class="feed">
  <h3><i></i>| Photo FEED</h3>
  <div class="prow"><span class="alt">Alva Sport</span><span>Kustlinje</span><span>Bergsö</span><span>Husgrund</span><span>Solvik</span><span class="alt">Fjällström</span><span>Glimt</span><span>Brovik</span><span class="alt">Norda26</span></div>
  <span class="btn">SHOW MORE</span>
</section>

<div class="social"><span>FOLLOW</span><span>PHOTO</span><span>PINS</span><span>PLUS</span><span>VIDEO</span><span>BLOG</span></div>
<nav class="fnav"><span>Products</span><span>Gallery</span><span>FAQ</span><span>Contact us</span></nav>

<footer class="footer">
  <div><h5>CONTACT US</h5>Formverk AB<br>Ekvägen 14<br>Box 123, Stockholm<br>Org. nr: 556000-0000</div>
  <div><h5>SIGN UP FOR NEWSLETTERS</h5>Få de senaste erbjudandena direkt.<div class="in"></div><span class="btn" style="margin-top:8px;padding:3px 12px;font-size:8px">SIGN UP</span></div>
  <div><h5>ABOUT</h5>Om oss<br>Villkor<br>Integritet</div>
  <div><h5>QUICK LINKS</h5>Priser<br>Galleri<br>Beställ<br>Kontakt</div>
  <div style="width:170px"><div class="brand"><i></i>Formverk</div>Vi skapar logotyper och grafisk design för lokala företag med snabb leverans och fasta priser.</div>
</footer>

</div>
</body>
</html>
```